Looking for a professional, clean and crisp business card

I am in the underground utilities industry and am just looking for a really impressive business card. I would like our card to be white with our symbol crisp and clear with it protruding. I also have a business partner that will require his name and info on the card once the design is set. I would like to have our website info on the card which is;
http://granitetrenchco.example/

Contact Information for Business Card

Website, contact name, number and email

```html
<!DOCTYPE html>
<html lang="en">
<head>
<meta charset="utf-8">
<title>Granite Trench Co – Business Card</title>
<link href="https://fonts.googleapis.com/css2?family=Arimo:wght@400;700&display=swap" rel="stylesheet">
<style>
  :root {
    --backdrop: #e4e4e4;
    --card-white: #f7f7f7;
    --ink: #231f20;
    --accent-blue: #2f5cb8;
    --accent-red: #e2262b;
    --rule-grey: #c9c9c9;
  }
  * { margin: 0; padding: 0; box-sizing: border-box; }
  html, body {
    width: 1200px; height: 930px; overflow: hidden;
    background: var(--backdrop);
    font-family: "Arimo", Arial, sans-serif;
  }
  .sheet {
    position: relative; width: 1200px; height: 930px;
    display: flex; flex-direction: column; align-items: center;
    justify-content: center; gap: 44px;
  }
  .card {
    position: relative; width: 700px; height: 400px;
    box-shadow: 0 6px 18px rgba(0,0,0,.12);
    overflow: hidden;
  }
  .card--front { background: var(--card-white); }
  .card--back { background: var(--ink); }

  /* band across the front */
  .band { position: absolute; left: 0; right: 0; top: 112px; height: 52px; }
  .band__rule { position: absolute; left: 0; right: 0; height: 2px; background: var(--ink); }
  .band__rule--top { top: 0; }
  .band__rule--bottom { bottom: 0; }
  .band__bar { position: absolute; left: 0; right: 0; top: 10px; height: 32px; background: var(--ink); }

  .brand {
    position: absolute; display: flex; align-items: center; gap: 12px;
    padding: 14px 22px;
  }
  .brand__dot { width: 18px; height: 18px; border-radius: 50%; background: var(--accent-blue); flex: none; }
  .brand__name { font-weight: 700; font-size: 26px; letter-spacing: 1px; text-transform: uppercase; white-space: nowrap; }
  .card--front .brand { left: 50%; top: 138px; transform: translate(-40%, -50%); background: var(--card-white); }
  .card--front .brand__name { color: var(--ink); }
  .card--back .brand { left: 50%; top: 50%; transform: translate(-50%, -50%); }
  .card--back .brand__name { color: #ffffff; font-size: 30px; }

  .person { position: absolute; left: 70px; top: 262px; text-align: right; width: 210px; }
  .person__name { font-weight: 700; font-size: 19px; color: var(--ink); letter-spacing: .5px; text-transform: uppercase; }
  .person__role { font-size: 16px; color: var(--accent-blue); margin-top: 4px; }

  .divider { position: absolute; left: 300px; top: 250px; width: 1px; height: 78px; background: var(--rule-grey); }

  .contact { position: absolute; left: 318px; top: 254px; list-style: none; }
  .contact__item { display: flex; align-items: center; gap: 9px; font-size: 16px; color: var(--ink); line-height: 24px; }
  .contact__icon { width: 15px; height: 15px; flex: none; }
</style>
</head>
<body>
<main class="sheet">
  <section class="card card--front" aria-label="Business card front">
    <div class="band">
      <div class="band__rule band__rule--top"></div>
      <div class="band__bar"></div>
      <div class="band__rule band__rule--bottom"></div>
    </div>
    <div class="brand">
      <span class="brand__dot"></span>
      <span class="brand__name">Granite Trench Co</span>
    </div>

    <div class="person">
      <p class="person__name">Marcus Hale</p>
      <p class="person__role">Managing Director</p>
    </div>
    <div class="divider"></div>
    <ul class="contact">
      <li class="contact__item">
        <svg class="contact__icon" viewBox="0 0 16 16"><path fill="var(--accent-red)" d="M3.6 1.2l2.3 2.6-1.2 1.9c.9 2 2.6 3.7 4.6 4.6l1.9-1.2 2.6 2.3-1.3 2.3C7.6 13.5 2.5 8.4 1.3 3.5z"/></svg>
        <span>044-987 650 321</span>
      </li>
      <li class="contact__item">
        <svg class="contact__icon" viewBox="0 0 16 16"><rect x="1" y="3" width="14" height="10" rx="1" fill="var(--accent-red)"/><path d="M1.5 3.8L8 9l6.5-5.2" fill="none" stroke="#fff" stroke-width="1.3"/></svg>
        <span>info@granitetrenchco.example</span>
      </li>
      <li class="contact__item">
        <svg class="contact__icon" viewBox="0 0 16 16"><circle cx="8" cy="8" r="7" fill="var(--accent-red)"/><g fill="none" stroke="#fff" stroke-width="1"><ellipse cx="8" cy="8" rx="3" ry="7"/><path d="M1 8h14M2.2 4.5h11.6M2.2 11.5h11.6"/></g></svg>
        <span>www.granitetrenchco.example</span>
      </li>
    </ul>
  </section>

  <section class="card card--back" aria-label="Business card back">
    <div class="brand">
      <span class="brand__dot"></span>
      <span class="brand__name">Granite Trench Co</span>
    </div>
  </section>
</main>
</body>
</html>
```